Ferncrest Dental, LLC business card project

Business card to be designed with current logo.
Dental office- please keep design of card that looks clean and professional.
Please include the following info:
Ferncrest Dental, LLC
Dr. Lorna Pettigrew
2871 Marlowe Street
Corbel Falls, CM 18093
610-555-0193
ferncrestdental.office@examplemail.test
Hello everyone-
Reason: Just got back from overseas- will look at all designs and provide feedback. Thank you!
Reason: Polling my friends for the final selection-
thank you to all those that participated- so many talented designers!

```html
<!DOCTYPE html>
<html lang="en">
<head>
<meta charset="utf-8">
<title>Ferncrest Dental, LLC – Business Card</title>
<link rel="stylesheet" href="https://fonts.googleapis.com/css2?family=Arimo:wght@400;700&display=swap">
<style>
  :root {
    --paper: #ffffff;
    --edge: #4a4a4a;
    --brand-green: #1ba35a;
    --leaf-green: #a8cf45;
    --doctor-red: #e0393e;
    --body-grey: #828487;
    --band-text: #ffffff;
  }
  html, body {
    margin: 0;
    padding: 0;
    width: 1200px;
    height: 668px;
    overflow: hidden;
    background: var(--paper);
  }
  .card {
    position: relative;
    width: 1200px;
    height: 668px;
    box-sizing: border-box;
    border: 2px solid var(--edge);
    background: var(--paper);
    overflow: hidden;
    font-family: "Arimo", Arial, sans-serif;
  }
  .brand {
    position: absolute;
    left: 196px;
    top: 52px;
    display: flex;
    align-items: center;
    gap: 28px;
  }
  .brand-dot {
    width: 70px;
    height: 70px;
    border-radius: 50%;
    background: var(--leaf-green);
  }
  .brand-name {
    margin: 0;
    font-size: 84px;
    font-weight: 400;
    line-height: 1;
    color: var(--brand-green);
    letter-spacing: -0.5px;
    white-space: nowrap;
  }
  .doctor {
    position: absolute;
    left: 172px;
    top: 258px;
    margin: 0;
    font-size: 29px;
    font-weight: 700;
    color: var(--doctor-red);
  }
  .contact {
    position: absolute;
    left: 172px;
    top: 345px;
    margin: 0;
    font-style: normal;
    font-size: 32px;
    line-height: 45px;
    color: var(--body-grey);
  }
  .contact .email {
    color: var(--brand-green);
  }
  .band {
    position: absolute;
    left: 0;
    bottom: 0;
    width: 1196px;
    height: 140px;
  }
  .band path {
    fill: var(--leaf-green);
  }
  .company {
    position: absolute;
    right: 100px;
    bottom: 34px;
    margin: 0;
    font-size: 31px;
    font-weight: 700;
    color: var(--band-text);
  }
</style>
</head>
<body>
  <div class="card">
    <header class="brand">
      <span class="brand-dot"></span>
      <h1 class="brand-name">Ferncrest Dental</h1>
    </header>

    <p class="doctor">Dr. Lorna Pettigrew</p>

    <address class="contact">
      <div>2871 Marlowe Street</div>
      <div>Corbel Falls, CM 18093</div>
      <div>610-555-0193</div>
      <div class="email">ferncrestdental.office@examplemail.test</div>
    </address>

    <svg class="band" viewBox="0 0 1196 140" preserveAspectRatio="none" aria-hidden="true">
      <path d="M0 140 L0 136 C 190 40, 500 4, 790 6 C 970 8, 1110 20, 1196 34 L1196 140 Z"/>
    </svg>

    <p class="company">Ferncrest Dental, LLC</p>
  </div>
</body>
</html>
```